Brivo Wellness Co Business Card for food and Beverage Wizards & Alchemists

One main business card design for a wellness enterprise which represents two brands. We need one primary card design, for two different employees. The only difference between the cards will be the name, title and phone number for each employee, all other design elements will be same.
I've uploaded the logos for each brand. I have also uploaded a mockup which I made using Google's drawing tool. I can provide example images of business cards we find attractive if you would like some help picturing what we like.
I'm picturing the color splash on the back of the card below the two logos to be a dark burgundy or blue. This may sound a bit silly but the feel of the card and color should look almost like wizard dress robes. Dark emerald green, dark blue and dark burgundy with black undertones and gold lace.

Target Market(s)

Healthy food and beverage industry

Industry/Entity Type

Health And Wellness

Contact Information for Business Card

On one side we would like the business name, location, title of employee, employee name and contact details. On the flip side we would like our two brand logos and a splash of color. We would like the card to have a black font with some gold accents if possible. We would also like the trim of the business card or a middle ply within the card stock to have a color other than white.

Font styles to use
Serif

Colors
ec1f27
0255a3
00a990

Requirements
Must have
• Bold dark colors, happy to provide sample photos of business cards I like from pinterest. Must have a version for two different employees. Must be sharp, modern and chic.
Nice to have
• Thick card stock layer in between the front and back of card that is either black or gold lace or something to make it feel, well let's say to make it feel expensive.
Should not have
• Should not have any cartoon-ey elements. All business.

```html
<!DOCTYPE html>
<html lang="en">
<head>
<meta charset="utf-8">
<title>Brivo Wellness Co — Business Cards</title>
<link href="https://fonts.googleapis.com/css2?family=Lato:wght@300;400;700&display=swap" rel="stylesheet">
<style>
  :root {
    --backdrop: #e3e2de;
    --paper: #f7f7f5;
    --ink: #1c1c1c;
    --ink-soft: #3a3a3a;
    --accent: #e8731e;
    --gold: #c9952f;
    --gold-deep: #a87722;
    --night: #222222;
    --emblem: #3b3b3b;
  }
  * { box-sizing: border-box; margin: 0; padding: 0; }
  html, body { width: 1200px; height: 1200px; overflow: hidden; }
  body {
    background: var(--backdrop);
    font-family: "Lato", sans-serif;
    color: var(--ink);
    position: relative;
  }
  .card {
    position: absolute;
    border: 4px solid var(--gold);
    box-shadow: 0 10px 24px rgba(0,0,0,0.12);
    overflow: hidden;
  }
  .card--front { width: 560px; height: 320px; background: var(--paper); left: 90px; }
  .card--front.first { top: 250px; }
  .card--front.second { top: 630px; }

  .brand-name {
    position: absolute; top: 40px; right: 36px;
    font-family: "Lato", sans-serif; font-weight: 400;
    font-size: 15px; letter-spacing: 5px; text-transform: uppercase;
    color: var(--ink-soft);
  }
  .person {
    position: absolute; left: 36px; top: 118px;
    padding-left: 14px; border-left: 5px solid var(--accent);
  }
  .person__name { font-size: 22px; font-weight: 300; line-height: 1.1; }
  .person__name strong { font-weight: 700; }
  .person__title { font-size: 13px; color: var(--accent); margin-top: 3px; }

  .contact { position: absolute; left: 40px; bottom: 34px; list-style: none; }
  .contact li {
    display: flex; align-items: center; gap: 10px;
    font-size: 13px; color: var(--ink-soft); line-height: 22px;
  }
  .contact svg { width: 13px; height: 13px; fill: var(--accent); flex: none; }

  .card--back {
    width: 400px; height: 700px; left: 720px; top: 250px;
    background: var(--night);
  }
  .emblem-area {
    position: absolute; left: 70px; top: 70px; width: 260px; height: 360px;
    background: radial-gradient(ellipse at center, var(--emblem) 0%, var(--night) 75%);
    border-radius: 8px;
  }
  .splash { position: absolute; left: 0; bottom: 0; width: 100%; height: 300px; }
</style>
</head>
<body>

  <section class="card card--front first">
    <div class="brand-name">Brivo Wellness Co</div>
    <div class="person">
      <div class="person__name">Marcus <strong>Hale</strong></div>
      <div class="person__title">Beverage Alchemist</div>
    </div>
    <ul class="contact">
      <li><svg viewBox="0 0 12 12"><path d="M6 0a4 4 0 0 0-4 4c0 3 4 8 4 8s4-5 4-8a4 4 0 0 0-4-4zm0 5.5A1.5 1.5 0 1 1 6 2.5a1.5 1.5 0 0 1 0 3z"/></svg>Larkvale, CA</li>
      <li><svg viewBox="0 0 12 12"><path d="M2.5 0 4.5 2.5 3.3 4a7 7 0 0 0 4.7 4.7L9.5 7.5 12 9.5 10.5 12A10.5 10.5 0 0 1 0 1.5z"/></svg>415.555.0142</li>
      <li><svg viewBox="0 0 12 12"><path d="M0 2h12v8H0zm1 1 5 4 5-4z"/></svg>hello@brivowellness.co</li>
    </ul>
  </section>

  <section class="card card--front second">
    <div class="brand-name">Brivo Wellness Co</div>
    <div class="person">
      <div class="person__name">Owen <strong>Castellan</strong></div>
      <div class="person__title">Cookie Wizard</div>
    </div>
    <ul class="contact">
      <li><svg viewBox="0 0 12 12"><path d="M6 0a4 4 0 0 0-4 4c0 3 4 8 4 8s4-5 4-8a4 4 0 0 0-4-4zm0 5.5A1.5 1.5 0 1 1 6 2.5a1.5 1.5 0 0 1 0 3z"/></svg>Larkvale, CA</li>
      <li><svg viewBox="0 0 12 12"><path d="M2.5 0 4.5 2.5 3.3 4a7 7 0 0 0 4.7 4.7L9.5 7.5 12 9.5 10.5 12A10.5 10.5 0 0 1 0 1.5z"/></svg>510.555.0187</li>
      <li><svg viewBox="0 0 12 12"><path d="M0 2h12v8H0zm1 1 5 4 5-4z"/></svg>hello@brivowellness.co</li>
    </ul>
  </section>

  <section class="card card--back">
    <div class="emblem-area" role="img" aria-label="Area for the two brand marks: flask emblem above a heraldic crest, in silver foil"></div>
    <svg class="splash" viewBox="0 0 400 300" preserveAspectRatio="none" role="img" aria-label="Gold colour splash sweeping across the lower card">
      <polygon points="0,150 400,40 400,300 0,300" fill="var(--gold)"/>
      <polygon points="0,210 400,120 400,135 0,228" fill="var(--gold-deep)" opacity="0.5"/>
    </svg>
  </section>

</body>
</html>
```